Covid19 Poster for workplaces

Create a poster on how to protect yourself from Corona virus at work.
We are a Brightside Wellbeing company. We have just re-branded so we need to fit in with our brand. We like clean and fresh, slightly amusing is ok if it will draw attention but it's an important topic. A4 and A3 please.

Content:

Headline: Lower the risk of COVID 19 in the workplace.

BE WELL

Bring your own cup - don’t share cups and food.
Elbow tap instead of handshakes and kisses
Wash your hands often - with soap.
Elbow or tissues when you cough or sneeze then straight in the bin
Leave your face alone after touching shared surfaces
Leave your bugs at home if you’re feeling unwell.

Call health line if you have a cough, a high temperature and shortness of breath. 0800 472 9160

Based on recommendations from ZPK and QLN

Target Market(s)

Employees - so anyone

Other font styles liked:
• Use the closest font to the brand documents

Requirements
Should not have
• Clip art

```html
<!DOCTYPE html>
<html lang="en">
<head>
<meta charset="utf-8">
<title>Wellbeing matters at work – Lower the risk of COVID-19</title>
<link rel="stylesheet" href="https://fonts.googleapis.com/css2?family=Montserrat:wght@700&family=PT+Sans:wght@400;700&display=swap">
<style>
  :root {
    --mint: #3fe6b9;
    --white: #ffffff;
    --ink: #1f2326;
    --photo-dark: #2a3a3c;
    --photo-mid: #4f6a73;
    --photo-warm: #c9a27a;
  }
  * { margin: 0; padding: 0; box-sizing: border-box; }
  html, body { width: 849px; height: 1200px; overflow: hidden; background: var(--white); }
  .poster {
    position: relative; width: 849px; height: 1200px; overflow: hidden;
    background: var(--white); font-family: "PT Sans", sans-serif; color: var(--ink);
  }
  .header-band { position: absolute; left: 0; top: 0; width: 849px; height: 333px; background: var(--mint); }
  .headline {
    position: absolute; left: 40px; top: 36px; color: var(--white);
    font-family: "Montserrat", sans-serif; font-weight: 700; font-size: 44px; line-height: 52px;
  }
  .subheadline {
    position: absolute; left: 40px; top: 211px; color: var(--white);
    font-family: "PT Sans", sans-serif; font-weight: 700; font-size: 33px; line-height: 44px;
  }
  .team-photo {
    position: absolute; left: 392px; top: 37px; width: 431px; height: 230px; border-radius: 40px;
    background: linear-gradient(120deg, var(--photo-warm) 0%, var(--photo-mid) 45%, var(--photo-dark) 100%);
    clip-path: polygon(0 0, 100% 0, 100% 55%, 70% 100%, 30% 100%, 0 45%);
  }
  .tips { position: absolute; left: 0; top: 0; width: 849px; height: 1009px; }
  .tip-text {
    position: absolute; width: 380px; text-align: center;
    font-size: 20px; line-height: 25px;
  }
  .tip-text.left { left: 23px; }
  .tip-text.right { left: 436px; }
  .tip-icon {
    position: absolute; width: 111px; height: 111px; border-radius: 50%; background: var(--mint);
  }
  .tip-icon.left { left: 150px; }
  .tip-icon.right { left: 558px; }
  .tip-icon svg { width: 111px; height: 111px; display: block; }
  .icon-line { fill: none; stroke: var(--ink); stroke-width: 2.6; stroke-linecap: round; stroke-linejoin: round; }
  .icon-line-light { fill: none; stroke: var(--white); stroke-width: 2.2; stroke-linecap: round; stroke-linejoin: round; }
  .footer-band { position: absolute; left: 0; top: 1009px; width: 849px; height: 191px; background: var(--mint); color: var(--white); }
  .brand-dot { position: absolute; left: 80px; top: 30px; width: 70px; height: 70px; border-radius: 50%; background: var(--white); }
  .brand-name {
    position: absolute; left: 165px; top: 34px;
    font-family: "PT Sans", sans-serif; font-weight: 700; font-size: 26px; line-height: 25px;
  }
  .brand-url { position: absolute; left: 74px; top: 96px; font-size: 15px; }
  .divider { position: absolute; left: 343px; top: 21px; width: 3px; height: 113px; background: var(--white); }
  .helpline { position: absolute; left: 371px; top: 30px; font-size: 20px; line-height: 28px; letter-spacing: 0.3px; }
  .helpline strong { font-weight: 700; }
  .source-note { position: absolute; left: 77px; top: 138px; font-size: 21px; letter-spacing: 0.4px; }
  .partner-badge-round { position: absolute; left: 562px; top: 112px; width: 63px; height: 63px; border-radius: 50%; border: 2px solid var(--white); }
  .partner-badge-rect { position: absolute; left: 635px; top: 128px; width: 127px; height: 40px; background: var(--white); }
</style>
</head>
<body>
<div class="poster">
  <header class="header-band">
    <h1 class="headline">Wellbeing<br>matters at<br>work</h1>
    <h2 class="subheadline">Lower the risk of COVID-19<br>in the workplace</h2>
    <div class="team-photo" role="img" aria-label="Photo of smiling colleagues working together at desks in an office"></div>
  </header>

  <section class="tips">
    <p class="tip-text left" style="top:358px">Bring your own cup, don’t share<br>cups and food</p>
    <p class="tip-text right" style="top:358px">Use your elbow or tissues when you cough<br>or sneeze then straight in the bin</p>
    <div class="tip-icon left" style="top:431px" role="img" aria-label="Icon of a steaming cup">
      <svg viewBox="0 0 111 111" aria-hidden="true">
        <path class="icon-line" d="M47 20c-3 4 3 7 0 11M55 20c-3 4 3 7 0 11M63 20c-3 4 3 7 0 11"/>
        <path class="icon-line" d="M38 43h36v10c0 10-8 17-18 17s-18-7-18-17z"/>
        <path class="icon-line" d="M74 45c7-2 10 5 5 10-2 3-5 4-8 5"/>
        <path class="icon-line" d="M33 74h48"/>
      </svg>
    </div>
    <div class="tip-icon right" style="top:431px" role="img" aria-label="Icon of a person sneezing into a tissue"></div>

    <p class="tip-text left" style="top:559px">Elbow tap instead of handshakes<br>and kisses</p>
    <p class="tip-text right" style="top:559px">Leave your face alone after touching<br>shared surfaces</p>
    <div class="tip-icon left" style="top:633px" role="img" aria-label="Icon of two arms touching elbows"></div>
    <div class="tip-icon right" style="top:633px" role="img" aria-label="Icon of a head beside a raised hand"></div>

    <p class="tip-text left" style="top:760px">Wash your hands often with soap<br>for at least 20 seconds</p>
    <p class="tip-text right" style="top:760px">Leave your bugs at home if you’re<br>feeling unwell</p>
    <div class="tip-icon left" style="top:840px" role="img" aria-label="Icon of hands being washed under a tap">
      <svg viewBox="0 0 111 111" aria-hidden="true">
        <path class="icon-line" d="M28 38V23h14v4H33v11zM33 27h30v10"/>
        <path class="icon-line" d="M56 37h14"/>
        <path class="icon-line-light" d="M60 44v3M64 44v3M60 52v3M64 52v3M58 60v3M66 60v3"/>
        <path class="icon-line-light" d="M46 84c-6 0-8-6-4-9l14-8c4-2 8 0 12 2h16M50 78h34"/>
      </svg>
    </div>
    <div class="tip-icon right" style="top:840px" role="img" aria-label="Icon of a house">
      <svg viewBox="0 0 111 111" aria-hidden="true">
        <path class="icon-line" d="M28 56l27-24 27 24"/>
        <path class="icon-line" d="M34 51v30h42V51"/>
        <path class="icon-line" d="M49 81V65h12v16"/>
        <path class="icon-line" d="M38 62h6v6h-6zM66 62h6v6h-6z"/>
        <path class="icon-line" d="M50 55a5 5 0 0 1 10 0z"/>
      </svg>
    </div>
  </section>

  <footer class="footer-band">
    <div class="brand-dot"></div>
    <div class="brand-name">Brightside<br>Wellbeing</div>
    <div class="brand-url">www.brightsidewellbeing.co.nz</div>
    <div class="divider"></div>
    <p class="helpline">Call careline if you have a cough,<br>a high temperature and shortness of breath.<br><strong>Ph: 0800 472 9160</strong></p>
    <p class="source-note">Based on recommendations from ZPK and QLN</p>
    <div class="partner-badge-round"></div>
    <div class="partner-badge-rect"></div>
  </footer>
</div>
</body>
</html>
```